ONE PAGE WEB DESIGN NEEDED for Finance Company

We need a web design (ONE PAGE DESIGN ONLY) for a new finance website called Brightwell Lending. Brightwell Lending helps customers get the right loan, whether its a home loan, investment loan, business loan etc.

You are required to come up with just the homepage design. Professionalism and quality is the key factors in the successful design.

Here are a few design questions to help you out:

-
What information should be used on the page?
Ive provided a document which outlines all the information needed to put on homepage (attached to the brief - called brightwell_page_info). Also see the Must Have section below on this brief.

-
What links should appear in the navigation/footer?:
The navigation should provide links to the following pages (NOTE: services link has subcategories):
1 Homepage
2 Services
- Home loans
- Investment loans
- Refinancing loans
- Business loans
3 About Us
4 FAQ
5 Contact Us

-
What colors should be used in the design?
Our company colors - Cyan: #2EADE3, Blue: #004B70, White. Feel free to submit designs with slight variations if you feel it improves the design.

-
What should the layout of the page be?
This is up to you to come up with - we are open to different layouts for the page design (as long as they capture the information effectively and making it easy to understand).

Target Market(s)

Potential Home owners, Families and Business Owners

Industry/Entity Type

Business

Requirements
Must have
• - Must contain our logo (attached as PNG and Illustrator file)
- Winning designer must supply a Photoshop file (PSD) that will allow us.
Nice to have
• - Should include photos/images of families, professional groups, tradespeople etc (you can use stock photos from PixQuarry and I will purchase them once you are selected as the winning design)
- Link to a loan calculator somewhere on front page with a button 'Find out how much you could borrow' (or maybe even try adding a loan calculator to the homepage if you think this would look good)
- Page should have a main headline "Finding the right loan for you" or "Brightwell Lending finds the right loan for our customers."
- Must include Accreditation logos somewhere on the homepage (will try and supply these soon)
Should not have
• - Poor quality designs will not be considered
- Do not use clipart

```html
<!DOCTYPE html>
<html lang="en">
<head>
<meta charset="utf-8">
<title>Brightwell Lending – Home</title>
<link href="https://fonts.googleapis.com/css2?family=Open+Sans:ital,wght@0,400;0,600;0,700;1,400&family=Noto+Serif:ital@1&display=swap" rel="stylesheet">
<style>
:root{
  --cyan:#2eade3;
  --cyan-light:#4fc3ee;
  --navy:#004b70;
  --ink:#0f4f6e;
  --grey:#7d8790;
  --grey-light:#a2a9af;
  --orange-top:#ffc33a;
  --orange-bot:#f19a0c;
  --green-top:#8cd031;
  --green-bot:#5ba40f;
  --footer:#4cc0ea;
  --white:#ffffff;
  --paper:#f8f7f3;
}
*{box-sizing:border-box;margin:0;padding:0}
html,body{width:949px;height:1200px;overflow:hidden}
body{position:relative;font-family:"Open Sans",Arial,sans-serif;color:var(--grey);background:var(--footer)}
.abs{position:absolute}
.backdrop{left:0;top:0;width:949px;height:1000px;
  background:linear-gradient(90deg,#c9cdd0 0%,#e7e9ea 12%,#f2f3f3 50%,#e2e4e4 85%,#b7b3ad 100%);}
.backdrop-fade{left:0;top:780px;width:949px;height:260px;background:linear-gradient(180deg,rgba(76,192,234,0) 0%,var(--footer) 80%)}

/* header */
.header{left:104px;top:0;width:741px;height:88px;background:var(--white);box-shadow:0 1px 4px rgba(0,0,0,.12)}
.brand{left:23px;top:42px;display:flex;align-items:center;gap:8px;font-size:18px;font-weight:600;color:var(--cyan);letter-spacing:-.3px}
.brand-dot{width:14px;height:14px;border-radius:50%;background:var(--cyan)}
.account-links{right:20px;top:22px;font-size:10px;color:var(--grey)}
.account-links span{margin:0 4px;color:var(--grey-light)}
.nav{left:244px;top:53px;display:flex;font-size:12px;font-weight:600;color:var(--navy)}
.nav a{display:block;height:22px;line-height:22px;padding:0 8px;margin-right:9px;text-decoration:none;color:var(--navy)}
.nav a.active{background:var(--cyan);color:var(--white)}
.hotline{left:592px;top:51px;display:flex;align-items:center;gap:7px;font-size:15px;font-weight:700;color:var(--cyan);letter-spacing:-.2px}
.hotline .bar{width:2px;height:14px;border-left:1px solid var(--cyan);border-right:1px solid var(--cyan)}

/* hero */
.hero{left:104px;top:102px;width:741px;height:367px;background-color:#f7f9fa;
  background-image:linear-gradient(rgba(0,75,112,.05) 1px,transparent 1px),linear-gradient(90deg,rgba(0,75,112,.05) 1px,transparent 1px);
  background-size:8px 8px;box-shadow:0 1px 4px rgba(0,0,0,.1)}
.hero-title{left:0;top:20px;width:741px;text-align:center;font-size:23px;font-weight:400;color:var(--ink);letter-spacing:-.2px}
.hero-intro{left:90px;top:55px;width:561px;text-align:center;font-size:10.5px;line-height:14px;color:var(--grey)}
.hero-photo{left:0;top:88px;width:360px;height:279px;background:linear-gradient(160deg,#eef1f3 0%,#c9d4dc 40%,#8d9aa5 70%,#e6eaed 100%)}
.offer{left:353px;top:130px;width:362px;height:196px;background:linear-gradient(180deg,var(--cyan-light),#1fa0d9)}
.offer-tail{left:326px;top:180px}
.btn-orange{display:flex;align-items:center;color:var(--white);background:linear-gradient(180deg,var(--orange-top),var(--orange-bot));border:1px solid #d98a07;border-radius:2px;box-shadow:0 1px 2px rgba(0,0,0,.2);text-decoration:none}
.btn-orange .bag{width:34px;height:100%;display:flex;align-items:center;justify-content:center;border-right:1px solid rgba(255,255,255,.45)}
.btn-orange .label{padding-left:9px;font-size:17px;letter-spacing:-.5px;white-space:nowrap}
.offer .btn-orange{position:absolute;left:27px;top:27px;width:215px;height:38px}
.offer-text{left:27px;top:74px;width:310px;font-size:10.5px;line-height:15px;color:var(--white);font-weight:600}
.offer-list{left:27px;top:128px;width:300px;display:grid;grid-template-columns:140px 150px;row-gap:7px;font-size:11px;color:var(--white)}
.offer-list li{list-style:none;display:flex;align-items:center;gap:6px}

/* welcome */
.welcome{left:104px;top:469px;width:741px;height:205px;background:var(--white)}
.welcome h2{position:absolute;left:27px;top:33px;font-size:18px;font-weight:400;color:var(--ink)}
.welcome .lead{position:absolute;left:27px;top:61px;width:430px;font-family:"Noto Serif",Georgia,serif;font-style:italic;font-size:12.5px;line-height:17px;color:#2c3940}
.welcome .body{position:absolute;left:27px;top:104px;width:435px;font-size:10px;line-height:15px;color:var(--grey-light)}
.help{left:501px;top:25px;width:218px;height:149px;background:linear-gradient(180deg,#16aadd,#1191cc);border-radius:2px}
.help h3{position:absolute;left:14px;top:14px;display:flex;align-items:center;gap:6px;font-size:12.5px;font-weight:700;color:var(--white)}
.help p{position:absolute;left:15px;top:35px;width:195px;font-size:9.5px;line-height:12px;color:var(--white)}
.help .field{position:absolute;left:19px;top:70px;width:186px;height:26px;display:flex;background:var(--white)}
.help .field span{flex:1;padding-left:8px;line-height:26px;font-size:10px;color:#b8bec2}
.help .field b{width:30px;background:#2a9a1a;color:var(--white);font-size:11px;line-height:26px;text-align:center}
.help .call{position:absolute;left:19px;top:104px;display:flex;align-items:center;gap:9px;color:var(--white)}
.help .call small{font-size:8.5px;font-weight:700;line-height:9px}
.help .call strong{font-size:23px;font-weight:700;letter-spacing:-.3px}

/* cta band */
.cta{left:97px;top:673px;width:755px;height:62px;background:#ececec;border-top:1px dashed #cfcfcf;border-bottom:1px dashed #cfcfcf;box-shadow:0 2px 4px rgba(0,0,0,.1)}
.cta h3{position:absolute;left:61px;top:10px;font-size:17.5px;font-weight:400;color:#3a3f43;letter-spacing:-.2px}
.cta p{position:absolute;left:61px;top:32px;font-size:10.5px;color:var(--grey)}
.cta .search{position:absolute;left:30px;top:17px}
.cta .btn-orange{position:absolute;left:497px;top:11px;width:230px;height:38px}

/* lower */
.lower{left:104px;top:735px;width:741px;height:255px;background:var(--paper)}
.calc{left:22px;top:49px;width:339px;height:123px;background:linear-gradient(90deg,#fff 60%,#dbe8f3);border:1px solid #dcdcdc}
.calc-device{left:10px;top:0;width:124px;height:121px;background:linear-gradient(180deg,#3a3d40,#8d9196 35%,#d0d3d5)}
.calc h3{position:absolute;left:161px;top:22px;display:flex;align-items:center;gap:5px;font-size:15px;font-weight:700;color:#3a3f43}
.btn-green{position:absolute;left:146px;top:51px;width:181px;height:48px;background:linear-gradient(180deg,var(--green-top),var(--green-bot));border-radius:2px;color:var(--white);font-size:14px;font-weight:600;line-height:16px;text-align:center;padding-top:8px}
.reviews{left:389px;top:55px;width:324px}
.reviews .head{display:flex;justify-content:space-between;align-items:center;font-size:11.5px;color:#3a3f43}
.reviews .head span{display:flex;align-items:center;gap:7px}
.reviews .head a{font-size:9px;color:#3a3f43;text-decoration:underline;margin-right:6px}
.quote{position:absolute;left:0;top:21px;width:324px;height:73px;background:var(--white);border:1px solid #dadada;box-shadow:0 1px 2px rgba(0,0,0,.08);padding:14px 16px;font-size:9.5px;line-height:13.5px;color:var(--navy)}
.quote-tail{left:268px;top:93px}
.reviews .who{position:absolute;left:210px;top:103px;font-size:9.5px;color:var(--navy)}

/* partners */
.partners{left:128px;top:951px;width:689px;height:70px;background:var(--white);box-shadow:0 2px 4px rgba(0,0,0,.12)}
.partners .row{position:absolute;left:28px;top:22px;display:flex;gap:28px}
.badge{width:64px;height:26px;background:#d9dcde;border-radius:2px}
.arrow{top:976px;width:22px;height:24px;background:var(--white);border:1px solid #d3d3d3;display:flex;align-items:center;justify-content:center}

/* footer */
.footer-col{top:1058px;font-size:9.5px;line-height:15px;color:var(--white)}
.footer-col h4{font-size:12px;font-weight:400;margin-bottom:6px}
.footer-col li{list-style:none}
.socials{display:flex;gap:6px;margin:4px 0 0 15px}
.socials i{display:block;width:12px;height:12px;border-radius:50%;background:var(--white);opacity:.9}
.rule{left:104px;top:1161px;width:741px;height:1px;background:rgba(255,255,255,.45)}
.copyright{left:104px;top:1169px;font-size:8px;color:var(--white)}
</style>
</head>
<body>
<div class="abs backdrop" role="img" aria-label="Softly blurred office interior backdrop"></div>
<div class="abs backdrop-fade"></div>

<header class="abs header">
  <div class="abs brand"><span class="brand-dot"></span>Brightwell Lending</div>
  <div class="abs account-links">Sign up<span>|</span>Member Login</div>
  <nav class="abs nav">
    <a class="active" href="#">Home</a><a href="#">Services</a><a href="#">About Us</a><a href="#">FAQ</a><a href="#">Contact Us</a>
  </nav>
  <div class="abs hotline"><span class="bar"></span>
    <svg width="18" height="13" viewBox="0 0 18 13"><path d="M1 5c0-3 4-4 8-4s8 1 8 4l-3 1-1-2H5L4 6Z M4 7h10l2 5H2Z" fill="#2eade3"/></svg>
    1800 246 810</div>
</header>

<section class="abs hero">
  <h1 class="abs hero-title">Brightwell Lending Finds The Right Loan For Our Customers</h1>
  <p class="abs hero-intro">Nemo enim ipsam voluptatem quia voluptas sit aspernatur aut odit aut fugit, sed quia consequuntur magni dolores eos qui ratione voluptatem sequi nesciunt. Neque porro quisquam est, qui.</p>
  <div class="abs hero-photo" role="img" aria-label="Photo of three smiling professionals at a meeting table"></div>
  <svg class="abs offer-tail" width="30" height="30" viewBox="0 0 30 30"><path d="M30 0V30L0 28Z" fill="#3cb9ea"/></svg>
  <div class="abs offer">
    <a class="btn-orange"><span class="bag"><svg width="12" height="16" viewBox="0 0 12 16"><path d="M3 1h6L7 4h0c3 2 5 5 5 8 0 3-3 4-6 4S0 15 0 12c0-3 2-6 5-8Z" fill="#fff"/></svg></span><span class="label">Find your Loan Now</span></a>
    <p class="abs offer-text">Nemo enim ipsam voluptatem quia voluptas sit aspernatur aut odit aut fugit, sed quia consequuntur magni dolores eos qui ratione voluptatem...</p>
    <ul class="abs offer-list">
      <li><svg width="11" height="9" viewBox="0 0 11 9"><path d="M1 5l3 3 6-7" stroke="#fff" stroke-width="2" fill="none"/></svg>Home loans</li>
      <li><svg width="11" height="9" viewBox="0 0 11 9"><path d="M1 5l3 3 6-7" stroke="#fff" stroke-width="2" fill="none"/></svg>Refinancing loans</li>
      <li><svg width="11" height="9" viewBox="0 0 11 9"><path d="M1 5l3 3 6-7" stroke="#fff" stroke-width="2" fill="none"/></svg>Investment loans</li>
      <li><svg width="11" height="9" viewBox="0 0 11 9"><path d="M1 5l3 3 6-7" stroke="#fff" stroke-width="2" fill="none"/></svg>Business loans</li>
    </ul>
  </div>
</section>

<section class="abs welcome">
  <h2>Welcome to Brightwell Lending</h2>
  <p class="lead">Nemo enim ipsam voluptatem quia voluptas sit aspernatur aut odit aut fugit, sed quia consequuntur magni dolores sequi nesciunt.</p>
  <p class="body">Neque porro quisquam est, qui. dolorem ipsum quia dolor sit amet, consectetur, adipisci velit, sed quia non numquam eius modi tempora incidunt ut labore et dolore magnam aliquam quaerat voluptatem. Neque porro quisquam est, qui. dolorem ipsum quia dolor sit amet, consectetur, adipisci velit, labore.</p>
  <div class="abs help">
    <h3><svg width="14" height="10" viewBox="0 0 14 10"><rect width="14" height="10" fill="#fff"/><path d="M0 0l7 6 7-6" stroke="#1591cc" fill="none"/></svg>GET HELP INSTANTLY</h3>
    <p>Neque porro quisquam est, qui. dolorem ipsum quia dolor sit amet.</p>
    <div class="field"><span>Email Address</span><b>Go</b></div>
    <div class="call"><small>CALL<br>NOW</small><strong>1847 302 915</strong></div>
  </div>
</section>

<section class="abs cta">
  <svg class="search" width="20" height="20" viewBox="0 0 20 20"><circle cx="8" cy="8" r="6" stroke="#3a3f43" stroke-width="2" fill="none"/><path d="M12.5 12.5L19 19" stroke="#3a3f43" stroke-width="3"/></svg>
  <h3>Find your perfect small business loan</h3>
  <p>Sign up now to get Started with your free account</p>
  <a class="btn-orange"><span class="bag"><svg width="12" height="16" viewBox="0 0 12 16"><path d="M3 1h6L7 4h0c3 2 5 5 5 8 0 3-3 4-6 4S0 15 0 12c0-3 2-6 5-8Z" fill="#fff"/></svg></span><span class="label">Find Your Perfect Loan</span></a>
</section>

<section class="abs lower">
  <div class="abs calc">
    <div class="abs calc-device" role="img" aria-label="Photo of a smartphone showing a calculator app"></div>
    <h3><svg width="15" height="15" viewBox="0 0 15 15"><circle cx="7.5" cy="7.5" r="7.5" fill="#5ba40f"/><path d="M4 8l2.5 2.5L11 5" stroke="#fff" stroke-width="2" fill="none"/></svg>Loan Calculator</h3>
    <a class="btn-green">Find out how much you<br>could borrow</a>
  </div>
  <div class="abs reviews">
    <div class="head"><span><svg width="12" height="10" viewBox="0 0 12 10"><path d="M0 0h12v7H5l-3 3V7H0Z" fill="#3a3f43"/></svg>Our Happy Customers</span><a href="#">View all</a></div>
    <blockquote class="quote">"All graduates are offered the opportunity to take their licensing test at our site. Ninety percent of Northgate Academy students go on to pass the exam!"</blockquote>
    <svg class="abs quote-tail" width="14" height="12" viewBox="0 0 14 12"><path d="M0 0h14L2 12Z" fill="#fff" stroke="#dadada"/><path d="M1 0h12" stroke="#fff" stroke-width="2"/></svg>
    <div class="who">Marla Quennet</div>
  </div>
</section>

<div class="abs partners" aria-label="Accreditation partners">
  <div class="row"><i class="badge"></i><i class="badge"></i><i class="badge"></i><i class="badge"></i><i class="badge"></i><i class="badge"></i><i class="badge"></i></div>
</div>
<div class="abs arrow" style="left:120px"><svg width="6" height="8" viewBox="0 0 6 8"><path d="M6 0v8L0 4Z" fill="#333"/></svg></div>
<div class="abs arrow" style="left:804px"><svg width="6" height="8" viewBox="0 0 6 8"><path d="M0 0v8l6-4Z" fill="#333"/></svg></div>

<footer>
  <div class="abs footer-col" style="left:105px"><h4>Navigate</h4><ul><li>How it Works</li><li>Success Stories</li><li>Loan Types</li><li>Article Library</li></ul></div>
  <div class="abs footer-col" style="left:220px"><h4>Services</h4><ul><li>Home Loan</li><li>Investment Loan</li><li>Refinancing</li><li>Business Loan</li></ul></div>
  <div class="abs footer-col" style="left:334px"><h4>Responsible</h4><ul><li>Responsible Lending</li><li>Financial Advise</li><li>Smart Choice</li></ul></div>
  <div class="abs footer-col" style="left:469px"><h4>About Us</h4><ul><li>FAQs</li><li>Testimonials</li><li>Our Blog</li></ul></div>
  <div class="abs footer-col" style="left:565px"><h4>Contact Us</h4><ul>
    <li><svg width="6" height="9" viewBox="0 0 6 9"><rect x=".5" y=".5" width="5" height="8" rx="1" stroke="#fff" fill="none"/></svg>&nbsp; 123-555-0190</li>
    <li><svg width="8" height="6" viewBox="0 0 8 6"><rect width="8" height="6" fill="#fff"/></svg>&nbsp; hello@brightwelllending.com</li></ul>
    <div class="socials"><i></i><i></i><i></i></div>
  </div>
  <div class="abs rule"></div>
  <div class="abs copyright">© copyright 2012 Brightwell Lending. All rights reserved.</div>
</footer>
</body>
</html>
```